Trucking/service truck *Updated

Cards for a trucking company. Company transfers logs to saw mills. We are looking for something edgy, modern and fun. It's very limited when it comes to trucking business card choices. Plus the owner also runs an on-site service truck. He has 20+ years mechanic experience.
Colors are open. Favorites are orange & purple, but not must have. We really want to emphasize trust, dependability and knowledge with a bright, attention getter.
On card:
Halvorsen & Halvorsen
Dale Halvorsen - Owner/Manager/Maintenance 555-214-0937
Tami Halvorsen -Office Administration/Bookkeeping 555-630-4518
4170 Maple Rd.
Oakvale, Kansas 66990
555-372-9061 - Office
Updates
Just a thought. Do you think you can combine the Taurus and Pisces signs? And put in the corner, or on the back or anything really? Thanks! You all or doing fantastic!

```html
<!DOCTYPE html>
<html lang="en">
<head>
<meta charset="utf-8">
<title>Halvorsen &amp; Halvorsen – Business Cards</title>
<link rel="stylesheet" href="https://fonts.googleapis.com/css2?family=Bebas+Neue&family=Oswald:wght@300&family=Open+Sans:wght@300;400&display=swap">
<style>
  :root {
    --navy: #07506f;
    --navy-deep: #064763;
    --truck-tone: #0b4a66;
    --orange: #f0712f;
    --teal-dark: #0a4550;
    --ink: #3c3c3c;
    --muted: #666666;
    --card-line: #e6e6e6;
    --frame: #3a3a3a;
    --paper: #ffffff;
  }
  * { box-sizing: border-box; margin: 0; padding: 0; }
  html, body { width: 1200px; height: 1000px; overflow: hidden; background: var(--paper); }
  .canvas {
    position: relative; width: 1200px; height: 1000px;
    border: 2px solid var(--frame); background: var(--paper); overflow: hidden;
  }
  .accent-bar { position: absolute; background: var(--navy); }
  .accent-bar--top-right { left: 1160px; top: 2px; width: 40px; height: 268px; }
  .accent-bar--bottom-left { left: 0; top: 733px; width: 39px; height: 265px; }

  .card {
    position: absolute; left: 310px; width: 580px; height: 352px;
    display: flex; border: 2px solid var(--card-line); border-left: none;
    overflow: hidden;
  }
  .card--dale { top: 135px; }
  .card--tami { top: 511px; }

  .brand-panel {
    position: relative; width: 257px; height: 100%; background: var(--navy);
  }
  .truck-art {
    position: absolute; left: 18px; top: 78px; width: 220px; height: 130px;
    background: linear-gradient(180deg, var(--navy) 0%, var(--truck-tone) 45%, var(--navy-deep) 100%);
    border-radius: 4px;
  }
  .company-name {
    position: absolute; left: 0; right: 28px; top: 214px;
    text-align: center; color: #fff;
    font-family: "Oswald", "Bebas Neue", sans-serif; font-weight: 300;
    font-size: 30px; line-height: 45px; text-transform: uppercase;
  }

  .details {
    position: relative; flex: 1; height: 100%; background: var(--paper);
    box-shadow: inset 14px 0 12px -10px rgba(0,0,0,0.18);
  }
  .person-name {
    position: absolute; left: 0; right: 0; top: 26px; text-align: center;
    font-family: "Bebas Neue", "Oswald", sans-serif; font-weight: 400; font-size: 39px;
    color: var(--navy-deep); letter-spacing: 0.3px; line-height: 1;
  }
  .person-role {
    position: absolute; left: 0; right: 0; top: 73px; text-align: center;
    font-family: "Open Sans", sans-serif; font-weight: 400; font-size: 17px;
    color: var(--muted); white-space: nowrap;
  }
  .contact-list { position: absolute; left: 0; top: 131px; list-style: none; }
  .contact-item { display: flex; align-items: center; height: 54px; }
  .contact-icon {
    width: 53px; height: 100%; flex: none; display: flex; align-items: center; justify-content: center;
  }
  .contact-icon--orange { background: var(--orange); }
  .contact-icon--dark { background: var(--teal-dark); }
  .contact-icon svg { width: 22px; height: 22px; }
  .contact-text {
    padding-left: 29px; font-family: "Open Sans", sans-serif; font-weight: 400;
    font-size: 20px; color: var(--ink); letter-spacing: 0.3px; white-space: nowrap;
  }
  .contact-text--address { font-size: 16.5px; line-height: 26px; padding-top: 2px; }
</style>
</head>
<body>
<div class="canvas">
  <div class="accent-bar accent-bar--top-right"></div>
  <div class="accent-bar accent-bar--bottom-left"></div>

  <section class="card card--dale">
    <div class="brand-panel">
      <div class="truck-art" role="img" aria-label="Line illustration of a dump truck in navy tones"></div>
      <p class="company-name">Halvorsen<br>&amp;<br>Halvorsen</p>
    </div>
    <div class="details">
      <h2 class="person-name">Dale Halvorsen</h2>
      <p class="person-role">Owner/Manager/Maintenance</p>
      <ul class="contact-list">
        <li class="contact-item">
          <span class="contact-icon contact-icon--orange">
            <svg viewBox="0 0 24 24"><rect x="7" y="2" width="10" height="20" rx="2" fill="none" stroke="#fff" stroke-width="2"/><rect x="9" y="5" width="6" height="9" fill="#fff"/></svg>
          </span>
          <span class="contact-text">555-214-0937</span>
        </li>
        <li class="contact-item">
          <span class="contact-icon contact-icon--dark">
            <svg viewBox="0 0 24 24"><path d="M7 3l3 4-2 2c1 2.5 3 4.8 5.5 6l2-2 4 3-2 3.5C11 19 5 12 4 5z" fill="#fff"/></svg>
          </span>
          <span class="contact-text">555-372-9061</span>
        </li>
        <li class="contact-item">
          <span class="contact-icon contact-icon--orange">
            <svg viewBox="0 0 24 24"><rect x="3" y="6" width="18" height="12" fill="none" stroke="#fff" stroke-width="1.6"/><path d="M3 6l9 7 9-7M3 18l7-6M21 18l-7-6" fill="none" stroke="#fff" stroke-width="1.6"/></svg>
          </span>
          <span class="contact-text">dalehal70@postline</span>
        </li>
        <li class="contact-item">
          <span class="contact-icon contact-icon--dark">
            <svg viewBox="0 0 24 24"><path d="M12 2a7 7 0 0 0-7 7c0 5 7 13 7 13s7-8 7-13a7 7 0 0 0-7-7zm0 10a3 3 0 1 1 0-6 3 3 0 0 1 0 6z" fill="#fff"/></svg>
          </span>
          <span class="contact-text contact-text--address">4170 Maple Rd.Oakvale,<br>Kansas 66990.</span>
        </li>
      </ul>
    </div>
  </section>

  <section class="card card--tami">
    <div class="brand-panel">
      <div class="truck-art" role="img" aria-label="Line illustration of a dump truck in navy tones"></div>
      <p class="company-name">Halvorsen<br>&amp;<br>Halvorsen</p>
    </div>
    <div class="details">
      <h2 class="person-name">Tami Halvorsen</h2>
      <p class="person-role">Office administration/Bookkeeping</p>
      <ul class="contact-list">
        <li class="contact-item">
          <span class="contact-icon contact-icon--orange">
            <svg viewBox="0 0 24 24"><rect x="7" y="2" width="10" height="20" rx="2" fill="none" stroke="#fff" stroke-width="2"/><rect x="9" y="5" width="6" height="9" fill="#fff"/></svg>
          </span>
          <span class="contact-text">555-630-4518</span>
        </li>
        <li class="contact-item">
          <span class="contact-icon contact-icon--dark">
            <svg viewBox="0 0 24 24"><path d="M7 3l3 4-2 2c1 2.5 3 4.8 5.5 6l2-2 4 3-2 3.5C11 19 5 12 4 5z" fill="#fff"/></svg>
          </span>
          <span class="contact-text">555-372-9061</span>
        </li>
        <li class="contact-item">
          <span class="contact-icon contact-icon--orange">
            <svg viewBox="0 0 24 24"><rect x="3" y="6" width="18" height="12" fill="none" stroke="#fff" stroke-width="1.6"/><path d="M3 6l9 7 9-7M3 18l7-6M21 18l-7-6" fill="none" stroke="#fff" stroke-width="1.6"/></svg>
          </span>
          <span class="contact-text">dalehal70@postline</span>
        </li>
        <li class="contact-item">
          <span class="contact-icon contact-icon--dark">
            <svg viewBox="0 0 24 24"><path d="M12 2a7 7 0 0 0-7 7c0 5 7 13 7 13s7-8 7-13a7 7 0 0 0-7-7zm0 10a3 3 0 1 1 0-6 3 3 0 0 1 0 6z" fill="#fff"/></svg>
          </span>
          <span class="contact-text contact-text--address">4170 Maple Rd.Oakvale,<br>Kansas 66990.</span>
        </li>
      </ul>
    </div>
  </section>
</div>
</body>
</html>
```